Roadwise Beacon Traffic Control Company Website

Modern website Wordpress design using all greyscale photos with a pop of red (such as road closure signs or detour cones) for strategic emphasis. (see brand guide for color codes)
The creative goal is to leverage high-contrast, desaturated imagery to create a clean, professional, and industrial feel. The selective use of red will draw immediate attention to critical elements—such as road hazards, safety equipment, or key messages to ensure the viewer's focus is directed with purpose.

Brand guide, homepage content and logo are attached. Create clean professional user experience to market services to industry professionals.

```html
<!DOCTYPE html>
<html lang="en">
<head>
<meta charset="UTF-8">
<title>Roadwise Beacon — Menu</title>
<link href="https://fonts.googleapis.com/css2?family=Archivo:wght@300;400&display=swap" rel="stylesheet">
<style>
  :root {
    --bg: #000000;
    --ink: #ffffff;
    --ink-dark: #111111;
    --accent: #e31e24;
  }
  * { margin: 0; padding: 0; box-sizing: border-box; }
  html, body {
    width: 1200px;
    height: 556px;
    overflow: hidden;
    background: var(--bg);
  }
  .menu-overlay {
    position: relative;
    width: 1200px;
    height: 556px;
    background: var(--bg);
    color: var(--ink);
    font-family: "Archivo", "Helvetica Neue", Arial, sans-serif;
    font-weight: 300;
  }
  .close-toggle {
    position: absolute;
    left: 70px;
    top: 73px;
    display: flex;
    align-items: center;
    gap: 15px;
    color: var(--ink);
    text-decoration: none;
  }
  .close-toggle__box {
    width: 40px;
    height: 40px;
    background: var(--ink);
    display: flex;
    align-items: center;
    justify-content: center;
  }
  .close-toggle__label {
    font-size: 12.5px;
    font-weight: 400;
    letter-spacing: 0.02em;
  }
  .brand {
    position: absolute;
    left: 50%;
    top: 93px;
    transform: translate(-50%, -50%);
    display: flex;
    align-items: center;
    gap: 8px;
    white-space: nowrap;
  }
  .brand__mark {
    width: 12px;
    height: 12px;
    background: var(--accent);
  }
  .brand__name {
    font-size: 17px;
    font-weight: 400;
    color: var(--ink);
    letter-spacing: 0.02em;
  }
  .cta-button {
    position: absolute;
    left: 1010px;
    top: 73px;
    width: 120px;
    height: 40px;
    background: var(--ink);
    color: var(--ink-dark);
    font-size: 12.5px;
    font-weight: 400;
    display: flex;
    align-items: center;
    justify-content: center;
    text-decoration: none;
  }
  .primary-nav {
    position: absolute;
    left: 69px;
    top: 174px;
    list-style: none;
  }
  .primary-nav a {
    display: block;
    color: var(--ink);
    text-decoration: none;
    font-size: 62px;
    line-height: 65px;
    letter-spacing: -0.01em;
  }
  .contact-details {
    position: absolute;
    right: 70px;
    top: 177px;
    text-align: right;
  }
  .contact-details a {
    display: block;
    color: var(--ink);
    text-decoration: none;
    font-size: 30px;
    line-height: 47px;
  }
  .secondary-nav {
    position: absolute;
    left: 0;
    right: 0;
    top: 465px;
    display: flex;
    justify-content: center;
    align-items: baseline;
    gap: 14px;
    font-size: 25px;
    font-weight: 400;
  }
  .secondary-nav a { color: var(--ink); text-decoration: none; }
</style>
</head>
<body>
  <div class="menu-overlay">
    <a class="close-toggle" href="#">
      <span class="close-toggle__box">
        <svg width="18" height="18" viewBox="0 0 18 18" aria-hidden="true">
          <path d="M1 1 L17 17 M17 1 L1 17" stroke="#333" stroke-width="1.4" fill="none"/>
        </svg>
      </span>
      <span class="close-toggle__label">CLOSE</span>
    </a>

    <div class="brand">
      <span class="brand__mark"></span>
      <span class="brand__name">Roadwise Beacon</span>
    </div>

    <a class="cta-button" href="#">Get in Touch</a>

    <ul class="primary-nav">
      <li><a href="#">Services</a></li>
      <li><a href="#">Rentals</a></li>
      <li><a href="#">Jobs</a></li>
    </ul>

    <div class="contact-details">
      <a href="#">(555) 014-2290</a>
      <a href="#">dana@roadwisebeacon.com</a>
    </div>

    <nav class="secondary-nav">
      <a href="#">About us</a>
      <span>.</span>
      <a href="#">Contacts</a>
    </nav>
  </div>
</body>
</html>
```